KTR Engineering Pty Ltd

I have already had Corvale welding and fabrication cards made , my business has changed too KTR engineering Pty Ltd so I need my logo changed on the cards
one side have my logo then the other side have what we do.
front side logo and details
owner /operator : Lachlan Meravic
email: ktr.works@ironvalemail.com
number: 0491537204
ABN: 47 261 538 902
ACN: 718 352 946
on back have in dot points what we do:
* structural steel erection
* precast panels
* site welding
*steel alteration & repair
* rigging & dogging
*labour hire
all details in breif

```html
<!DOCTYPE html>
<html lang="en">
<head>
<meta charset="utf-8">
<title>KTR Engineering Pty Ltd – Business Card</title>
<link href="https://fonts.googleapis.com/css2?family=Arimo:wght@400;700&display=swap" rel="stylesheet">
<style>
  :root {
    --maroon: #8b3a2f;
    --navy: #15223a;
    --paper: #f4f4f2;
    --ink: #1b2438;
    --stage: #2a2a2c;
    --on-maroon: #f3e4df;
  }
  * { margin: 0; padding: 0; box-sizing: border-box; }
  html, body { width: 1200px; height: 874px; overflow: hidden; }
  body {
    background: var(--stage);
    font-family: "Arimo", Arial, sans-serif;
    position: relative;
  }
  .card {
    position: absolute;
    left: 300px;
    width: 600px;
    height: 343px;
    border-radius: 18px;
    overflow: hidden;
  }
  .card--back { top: 64px; background: var(--maroon); }
  .card--front { top: 467px; background: var(--paper); }
  .card-shapes { position: absolute; inset: 0; width: 100%; height: 100%; }

  .brand {
    position: absolute;
    display: flex; align-items: center; justify-content: center; gap: 10px;
  }
  .brand-mark { width: 14px; height: 14px; border-radius: 50%; flex: none; }
  .brand-name { font-weight: 700; font-size: 26px; letter-spacing: 0.3px; white-space: nowrap; }
  .brand-phone {
    position: absolute; text-align: center;
    font-size: 14px; font-weight: 700; letter-spacing: 1px;
  }

  /* back */
  .card--back .brand { left: 0; right: 0; top: 96px; }
  .card--back .brand-mark { background: var(--on-maroon); }
  .card--back .brand-name { color: var(--on-maroon); }
  .card--back .brand-phone { left: 0; right: 0; top: 136px; color: var(--on-maroon); }
  .services {
    position: absolute; left: 30px; right: 30px; top: 196px;
    list-style: none; display: flex; flex-wrap: wrap; justify-content: center;
    column-gap: 10px; row-gap: 10px;
    color: var(--on-maroon); font-size: 17px;
  }
  .services li::before { content: "•"; margin-right: 10px; }
  .services li:first-child::before,
  .services li.break + li::before { content: none; }
  .services .break { flex-basis: 100%; height: 0; }
  .services .break::before { content: none; }

  /* front: content centred in the white area */
  .card--front .brand { left: 60px; width: 400px; top: 74px; }
  .card--front .brand-mark { background: var(--maroon); }
  .card--front .brand-name { color: var(--ink); font-size: 24px; }
  .card--front .brand-phone { left: 60px; width: 400px; top: 112px; color: var(--maroon); font-size: 13px; }
  .holder { position: absolute; left: 60px; width: 400px; top: 146px; text-align: center; }
  .holder-name { font-size: 23px; font-weight: 700; color: var(--ink); }
  .holder-role { font-size: 15px; color: var(--maroon); margin-top: 2px; }
  .details {
    position: absolute; left: 205px; top: 222px;
    font-size: 15px; color: var(--ink); line-height: 1.6;
  }
  .details .row { display: flex; align-items: center; gap: 8px; white-space: nowrap; }
  .details svg { width: 13px; height: 13px; fill: var(--ink); flex: none; }
</style>
</head>
<body>

<section class="card card--back" aria-label="Card back">
  <div class="brand"><span class="brand-mark"></span><span class="brand-name">KTR Engineering Pty Ltd</span></div>
  <div class="brand-phone">0491537204</div>
  <ul class="services">
    <li>Structural steel erection</li>
    <li>Precast panels</li>
    <li>Site welding</li>
    <li class="break" aria-hidden="true"></li>
    <li>Steel alteration &amp; repair</li>
    <li>Rigging &amp; dogging</li>
    <li>Labour hire</li>
  </ul>
</section>

<section class="card card--front" aria-label="Card front">
  <svg class="card-shapes" viewBox="0 0 600 343" preserveAspectRatio="none" aria-hidden="true">
    <path d="M0 0 H24 C45 150 100 270 165 343 H0 Z" fill="var(--navy)"/>
    <path d="M600 0 H420 C495 80 545 200 535 343 H600 Z" fill="var(--maroon)"/>
  </svg>
  <div class="brand"><span class="brand-mark"></span><span class="brand-name">KTR Engineering Pty Ltd</span></div>
  <div class="brand-phone">0491537204</div>
  <div class="holder">
    <div class="holder-name">Lachlan Meravic</div>
    <div class="holder-role">owner /operator</div>
  </div>
  <div class="details">
    <div class="row">ABN: 47 261 538 902 &nbsp;|&nbsp; ACN: 718 352 946</div>
    <div class="row">
      <svg viewBox="0 0 24 24"><path d="M6.6 10.8a15 15 0 0 0 6.6 6.6l2.2-2.2a1 1 0 0 1 1-.25 11.4 11.4 0 0 0 3.6.57 1 1 0 0 1 1 1V20a1 1 0 0 1-1 1A17 17 0 0 1 3 4a1 1 0 0 1 1-1h3.5a1 1 0 0 1 1 1c0 1.25.2 2.45.57 3.57a1 1 0 0 1-.25 1z"/></svg>
      0491537204
    </div>
    <div class="row">
      <svg viewBox="0 0 24 24"><path d="M2 5h20v14H2z M2 5l10 8 10-8" fill="none" stroke="var(--ink)" stroke-width="2"/></svg>
      ktr.works@ironvalemail.com
    </div>
  </div>
</section>

</body>
</html>
```